Visitenkarten-Design für Psychiaterin
Zielgruppe
Dr. med. Monika Haberl, Ärztin, Psychotherapie für Kinder Jugendliche und Erwachsene, spezialisiert auf komplexe Posttraumatische Belastungsstörung, Dissoziative Störungen, Persönlichkeitsstörungen, Bindungsstörungen, LUMO-Mentorin
Das Design soll modern sein, Seriosität Professionalität, Dynamik und Geborgenheit ausstrahlen. Zielgruppe sind Menschen die traumatische Situationen überlebt haben.
Aufgabenstellung
Name, Fachgebiet und Spezialisierung, Telefonnummer, e-Mail
Unter Dateiupload sind Visitenkartenbeispiele die mir gefallen

```html
<!DOCTYPE html>
<html lang="de">
<head>
<meta charset="utf-8">
<title>Visitenkarte – Dr. med. Monika Haberl</title>
<link href="https://fonts.googleapis.com/css2?family=Montserrat:wght@400;500&family=Merriweather:wght@400&family=Hind:wght@400&display=swap" rel="stylesheet">
<style>
  :root {
    --bg: #e4e9e9;
    --card: #ffffff;
    --ink: #3a3a3a;
    --ink-soft: #555555;
    --rose: #e7bdb4;
    --rose-pale: #f7e3de;
    --rose-faint: rgba(240, 200, 192, 0.28);
  }
  * { margin: 0; padding: 0; box-sizing: border-box; }
  html, body {
    width: 1200px; height: 900px; overflow: hidden;
    background: var(--bg);
  }
  .sheet {
    width: 1200px; height: 900px;
    display: flex; flex-direction: column; align-items: center; justify-content: center;
    gap: 40px;
  }
  .card {
    position: relative;
    width: 680px; height: 400px;
    background: var(--card);
    overflow: hidden;
    box-shadow: 0 2px 10px rgba(0,0,0,0.08);
  }
  .wash-large {
    position: absolute;
    width: 360px; height: 360px; border-radius: 50%;
    background: radial-gradient(circle, var(--rose-faint) 0%, rgba(240,200,192,0.2) 55%, rgba(240,200,192,0) 72%);
  }
  .card--front .wash-large { right: -60px; top: -90px; }
  .card--back .wash-large { right: -80px; top: -70px; }

  /* front */
  .front-title {
    position: absolute; left: 120px; top: 168px;
  }
  .wash-small {
    position: absolute; left: -42px; top: -28px;
    width: 110px; height: 110px; border-radius: 50%;
    background: radial-gradient(circle, rgba(231,189,180,0.55) 0%, rgba(231,189,180,0.35) 50%, rgba(231,189,180,0) 72%);
  }
  .front-name {
    position: relative;
    font-family: "Montserrat", sans-serif; font-weight: 400;
    font-size: 34px; letter-spacing: 0.5px; color: var(--ink);
    white-space: nowrap;
  }
  .front-sub {
    position: relative;
    font-family: "Merriweather", serif; font-size: 14.5px;
    color: var(--ink-soft); margin-top: 4px; margin-left: 22px;
  }

  /* back */
  .accent-bar {
    position: absolute; left: 62px; top: 0;
    width: 60px; height: 148px;
    background: var(--rose);
    border-radius: 0 0 30px 30px;
  }
  .icon-badge {
    position: absolute; width: 44px; height: 44px; border-radius: 50%;
    background: var(--rose);
    display: flex; align-items: center; justify-content: center;
  }
  .accent-bar .icon-badge { left: 8px; bottom: 8px; background: transparent; }
  .badge-phone { left: 70px; top: 172px; }
  .badge-web { left: 70px; top: 232px; }
  .badge-tick { left: 70px; top: 292px; }
  .back-name {
    position: absolute; left: 150px; top: 44px;
    font-family: "Montserrat", sans-serif; font-weight: 400;
    font-size: 32px; letter-spacing: 0.5px; color: var(--ink);
  }
  .back-title {
    position: absolute; left: 170px; top: 90px;
    font-family: "Montserrat", sans-serif; font-size: 15px; color: var(--ink-soft);
  }
  .contact-line {
    position: absolute; left: 150px;
    font-family: "Hind", sans-serif; font-size: 18px; color: var(--ink);
  }
  .contact-phone { top: 130px; }
  .contact-web { top: 180px; left: 170px; }
  .specialties {
    position: absolute; left: 150px; top: 240px; width: 500px;
    font-family: "Hind", sans-serif; font-size: 16px; line-height: 1.4; color: var(--ink);
  }
</style>
</head>
<body>
<main class="sheet">
  <section class="card card--front">
    <div class="wash-large" role="img" aria-label="Zarter rosa Aquarellkreis als Hintergrundmotiv"></div>
    <div class="front-title">
      <div class="wash-small" role="img" aria-label="Kleiner rosa Aquarellkreis hinter dem Namen"></div>
      <h1 class="front-name">Dr. med. MONIKA HABERL</h1>
      <p class="front-sub">Psychotherapie für Kinder Jugendliche und Erwachsene</p>
    </div>
  </section>

  <section class="card card--back">
    <div class="wash-large" role="img" aria-label="Zarter rosa Aquarellkreis als Hintergrundmotiv"></div>
    <div class="accent-bar">
      <span class="icon-badge">
        <svg width="22" height="22" viewBox="0 0 22 22" aria-hidden="true">
          <circle cx="11" cy="7" r="4.5" fill="#fff"/>
          <path d="M2 20c0-5 4-8 9-8s9 3 9 8z" fill="#fff"/>
        </svg>
      </span>
    </div>
    <span class="icon-badge badge-phone">
      <svg width="22" height="22" viewBox="0 0 22 22" aria-hidden="true">
        <path d="M3 8c0-3 3-4 8-4s8 1 8 4v1h-4V7H7v2H3z" fill="none" stroke="#fff" stroke-width="1.6"/>
        <rect x="5" y="10" width="12" height="8" rx="2" fill="none" stroke="#fff" stroke-width="1.6"/>
        <circle cx="11" cy="14" r="2" fill="#fff"/>
      </svg>
    </span>
    <span class="icon-badge badge-web">
      <svg width="22" height="22" viewBox="0 0 22 22" aria-hidden="true">
        <circle cx="11" cy="11" r="8" fill="none" stroke="#fff" stroke-width="1.6"/>
        <ellipse cx="11" cy="11" rx="3.5" ry="8" fill="none" stroke="#fff" stroke-width="1.4"/>
        <line x1="3" y1="11" x2="19" y2="11" stroke="#fff" stroke-width="1.4"/>
        <line x1="5" y1="7" x2="17" y2="7" stroke="#fff" stroke-width="1.2"/>
        <line x1="5" y1="15" x2="17" y2="15" stroke="#fff" stroke-width="1.2"/>
      </svg>
    </span>
    <span class="icon-badge badge-tick">
      <svg width="22" height="22" viewBox="0 0 22 22" aria-hidden="true">
        <path d="M6 11l4 4 7-8" fill="none" stroke="#fff" stroke-width="2" stroke-linecap="round" stroke-linejoin="round"/>
      </svg>
    </span>

    <h2 class="back-name">MONIKA HABERL</h2>
    <p class="back-title">Dr. med.</p>
    <p class="contact-line contact-phone" style="top:128px;left:190px">+012 345 6780</p>
    <p class="contact-line contact-web" style="top:182px;left:140px">www.praxis-haberl.de</p>
    <p class="specialties" style="left:140px">Psychotherapie für Kinder Jugendliche und Erwachsene, spezialisiert auf komplexe Posttraumatische Belastungsstörung, Dissoziative Störungen, Persönlichkeitsstörungen, Bindungsstörungen, LUMO-Mentorin</p>
  </section>
</main>
</body>
</html>
```